Poster Design Project

About Us
Brimco is a company that specializes in providing communication solutions to the travel market. Our simple vision of “every hotel should have a mobile phone in the guest rooms”, led us to develop a path breaking cost effective mobile phone. With full integration capabilities with the hotels property management system, location based marketing, user locator and other features, this product is unique in addressing the hospitality segment.
Product Placement
The Brimco mobile will be placed in the hotel room on an A4 Sized transparent stand (the transparent stand is attached for your reference. If you notice, the phone will be placed in the jacket on the bottom left and in another jacket on the bottom right will be the brochure. So effectively, the design space available on the A4 brochure is only 60% of the space). The designed poster that we wish designed will be inserted in the A4 sized acrylic stand. The stand would typically be on the bedside table or on the study table of the hotel room. The A4 design should be bright and vibrant in keeping with our logo colors.
Attached is our logo. Also attached is the symbol of our phone that could be used innovatively on the brochure if you think it helps.
Attached is the content for the poster.
Reason: Feedback from the management team got delayed, hence the extension. Thanks
Reason: The delay is in the content finalization.

```html
<!DOCTYPE html>
<html lang="en">
<head>
<meta charset="utf-8">
<title>Brimco – Keep Talking</title>
<link rel="stylesheet" href="https://fonts.googleapis.com/css2?family=Nunito:wght@800&family=Carlito:wght@700&display=swap">
<style>
  :root {
    --paper: #f4e39c;
    --brand-orange: #f7a12a;
    --soft-orange: #f5a94a;
    --hot-pink: #e61f5e;
    --sleeve-line: #6f6a5e;
    --brochure-card: #e3d4ba;
    --white: #ffffff;
    --device-dark: #1b1c1f;
    --device-mid: #3a3d44;
  }
  * { margin: 0; padding: 0; box-sizing: border-box; }
  html, body { width: 848px; height: 1200px; overflow: hidden; background: var(--paper); }
  .poster {
    position: relative; width: 848px; height: 1200px;
    background: var(--paper);
    font-family: "Carlito", "Calibri", Arial, sans-serif; font-weight: 700;
  }
  .abs { position: absolute; }
  .center-text { text-align: center; }

  .brand-dot {
    left: 25px; top: 22px; width: 190px; height: 190px; border-radius: 50%;
    background: var(--brand-orange);
  }
  .brand-name {
    left: 232px; top: 8px;
    font-family: "Nunito", Arial, sans-serif; font-weight: 800;
    font-size: 172px; line-height: 1; letter-spacing: -2px;
    color: var(--brand-orange);
  }

  .headline {
    left: 100px; width: 654px; top: 196px;
    color: var(--hot-pink); font-size: 38px; line-height: 54px;
  }

  .badge {
    display: flex; align-items: center; justify-content: center;
    border-radius: 50%; color: var(--white); text-align: center;
  }
  .badge-quality {
    left: 684px; top: 206px; width: 138px; height: 138px;
    background: var(--brand-orange); font-size: 25px; line-height: 30px;
    transform: rotate(22deg);
  }
  .badge-bill {
    left: 33px; top: 525px; width: 162px; height: 162px;
    background: var(--hot-pink); font-size: 26px; line-height: 31px;
  }

  .offer-list {
    left: 90px; width: 660px; top: 351px;
    list-style: none; color: var(--soft-orange);
    font-size: 31px; line-height: 46.5px;
  }

  .tagline {
    left: 300px; width: 430px; top: 615px;
    color: var(--hot-pink); font-size: 42px; line-height: 52px;
  }

  .sleeve { border: 1.5px solid var(--sleeve-line); }
  .sleeve-left { left: 47px; top: 755px; width: 265px; height: 412px; }
  .sleeve-right { left: 527px; top: 755px; width: 268px; height: 412px; }

  .brochure-card {
    left: 54px; top: 687px; width: 248px; height: 474px;
    background: var(--brochure-card); border: 1.5px solid var(--sleeve-line);
  }
  .brochure-dot {
    left: 156px; top: 719px; width: 38px; height: 38px; border-radius: 50%;
    background: var(--brand-orange);
  }
  .brochure-name {
    left: 54px; width: 248px; top: 774px;
    color: var(--soft-orange); font-size: 54px; line-height: 58px;
  }
  .brochure-label {
    left: 54px; width: 248px; top: 834px;
    color: var(--soft-orange); font-size: 29px; line-height: 32px;
  }

  .plan-note {
    left: 315px; width: 220px; top: 702px;
    color: var(--soft-orange); font-size: 32px; line-height: 44.5px;
  }
  .details-note {
    left: 330px; width: 190px; top: 988px;
    color: var(--soft-orange); font-size: 25px; line-height: 35.5px;
  }

  .device-visual {
    left: 550px; top: 695px; width: 228px; height: 463px; border-radius: 34px;
    background: linear-gradient(180deg, var(--device-mid) 0%, var(--device-dark) 45%, var(--device-mid) 100%);
  }
</style>
</head>
<body>
<main class="poster">
  <div class="abs brand-dot" aria-hidden="true"></div>
  <h1 class="abs brand-name">Brimco</h1>

  <p class="abs headline center-text">Pick up this phone NOW,<br>to keep talking....</p>

  <div class="abs badge badge-quality"><span>Excellent<br>Call<br>Quality</span></div>

  <ul class="abs offer-list center-text">
    <li>SAVE 80% on international roaming</li>
    <li>Get a LOCAL number</li>
    <li>60 FREE minutes of international Calls</li>
    <li>60 FREE minutes of local calls</li>
    <li>= 499 BHT</li>
  </ul>

  <div class="abs badge badge-bill"><span>Itemised<br>Bill on<br>Checkout</span></div>

  <p class="abs tagline center-text">Brimco, Keep Talking</p>

  <div class="abs brochure-card"></div>
  <div class="abs brochure-dot" aria-hidden="true"></div>
  <p class="abs brochure-name center-text">Brimco</p>
  <p class="abs brochure-label center-text">Brochure</p>
  <div class="abs sleeve sleeve-left"></div>

  <p class="abs plan-note center-text">Flexible<br>Tariff Plan<br>for you<br>to choose<br>from</p>
  <p class="abs details-note center-text">Please<br>refer to the<br>Brochure<br>for more<br>details</p>

  <div class="abs device-visual" role="img" aria-label="Photo of the in-room smartphone with keyboard, standing in its clear sleeve"></div>
  <div class="abs sleeve sleeve-right"></div>
</main>
</body>
</html>
```